Refresh Application User Interface

Brindlecove wishes to update the look of its business applications. Two representative forms are shown below. Please note, we are not considering changes in functionality or usability. Our goal is a cleaner, more contemporary design.

Industry/Entity Type

Business

```html
<!DOCTYPE html>
<html lang="en">
<head>
<meta charset="utf-8">
<title>Purchase Order Lines – Brindlecove</title>
<link href="https://fonts.googleapis.com/css2?family=Open+Sans:wght@400;600;700&family=Arimo:wght@400;700&display=swap" rel="stylesheet">
<style>
:root{
  --ink:#222;
  --title:#4a4a4a;
  --topbar:#000;
  --brand:#1a86dc;
  --nav:#2196ee;
  --tab-bg:#e4e4e4;
  --tool:#4f5d68;
  --tool-dark:#43515c;
  --panel:#f3f3f3;
  --line:#c9c9c9;
  --field:#eeeeee;
  --field-text:#1a237e;
  --green:#1f8a2e;
  --blue-link:#1a1aff;
  --status:#fdfce4;
  --status-line:#e8e2a8;
  --lock:#f6e48a;
}
*{box-sizing:border-box;margin:0;padding:0}
html,body{width:1200px;height:897px;overflow:hidden;background:#fff}
.stage{position:relative;width:1086px;height:791px;transform:scale(1.105,1.134);transform-origin:0 0;font-family:"Open Sans",sans-serif;color:var(--ink)}
.abs{position:absolute}

.topbar{left:0;top:0;width:1086px;height:28px;background:var(--topbar);color:#fff;font-size:13px}
.topbar .user{left:20px;top:5px}
.topbar b{font-weight:700}
.topbar .sep{margin:0 0 0 6px}
.topbar .role{left:212px;top:5px}
.topbar .util{right:10px;top:0;display:flex;height:28px}
.topbar .util span{padding:5px 9px 0;border-left:1px solid #444}
.topbar .util span:first-child{border-left:none}

.modules{left:20px;top:40px;display:flex;height:29px}
.modules span{background:var(--tab-bg);color:#444;font-weight:600;font-size:14px;padding:5px 11px 0;margin-right:1px;border-radius:3px 3px 0 0}
.modules .on{background:var(--brand);color:#fff}
.brandname{left:866px;top:30px;font-size:31px;font-weight:700;color:var(--brand);letter-spacing:.5px;font-family:"Open Sans",sans-serif}

.subnav{left:0;top:69px;width:1086px;height:30px;background:var(--nav);display:flex;align-items:center;padding-left:20px;color:#fff;font-size:13px;font-weight:600}
.subnav span{padding:0 8px}
.subnav .on{background:#fff;color:var(--brand);border-radius:10px;padding:1px 8px}
.subnav .gap{border-left:1px solid #7fc0f4;height:16px;padding:0;margin:0 6px}

.pagetitle{left:20px;top:108px;font-size:22px;font-weight:600;color:var(--title)}
.pagetabs{left:808px;top:109px;display:flex;height:30px}
.pagetabs span{background:#efefef;color:#333;font-size:14px;padding:5px 9px 0;margin-right:2px;border-radius:3px 3px 0 0;position:relative}
.pagetabs .on{background:var(--tool);color:#fff}
.pagetabs .ok::after{content:"";position:absolute;right:-2px;top:0;width:8px;height:8px;border-radius:50%;background:#5cb85c}

.toolbar{left:20px;top:139px;width:1046px;height:30px;background:var(--tool);color:#fff;font-size:13px}
.toolbar .item{position:absolute;top:7px;display:flex;align-items:center;gap:5px}
.toolbar .dim{color:#a5adb3}
.toolbar .div{position:absolute;top:4px;width:1px;height:22px;background:#66747e}

.form{left:32px;top:179px;width:1023px;height:558px;background:var(--panel);border:1px solid var(--line)}
.lbl{position:absolute;font-family:"Arimo",sans-serif;font-size:13px;color:#111;text-align:right}
.val{position:absolute;height:20px;background:var(--field);font-family:"Arimo",sans-serif;font-size:13px;padding:2px 4px;color:#222}
.green{color:var(--green);font-size:14px;font-family:"Arimo",sans-serif}
.note{color:var(--blue-link);font-family:"Arimo",sans-serif;font-size:14px}

.inner{left:50px;top:396px;width:987px;height:321px;background:#fff;border:1px solid #ddd}
.ftabs{left:50px;top:396px;display:flex;height:29px;border-bottom:1px solid #ddd;width:987px}
.ftabs span{font-size:14px;padding:5px 14px 0;border-right:1px solid #ddd;color:#222}
.ftabs .on{border-bottom:2px solid var(--brand)}
.sel{position:absolute;height:20px;background:#fff;border:1px solid #888;font-family:"Arimo",sans-serif;font-size:13px;color:var(--field-text);padding:1px 3px}
.sel::after{content:"";position:absolute;right:0;top:0;width:19px;height:18px;border-left:1px solid #999;background:#fafafa}
.sel svg{position:absolute;right:4px;top:5px;z-index:1}
.req{position:absolute;color:#999;font-size:15px}

.status{left:31px;top:749px;width:1025px;height:26px;background:var(--status);border:1px solid var(--status-line);font-size:14px;text-align:center;padding-top:3px;color:#333}
</style>
</head>
<body>
<div class="stage">

  <div class="abs topbar">
    <div class="abs user">Logged In As <b>Dana Whitlow</b> <span class="sep">⚙</span></div>
    <div class="abs role">Current Role <b>administrator</b> <span class="sep">▾</span></div>
    <div class="abs util"><span>Touch</span><span>New Tab</span><span>Help</span><span>Support</span><span>Log Out</span></div>
  </div>

  <nav class="abs modules"><span>Home</span><span>eSource</span><span class="on">eBuy</span><span>eRequest</span><span>eSell</span><span>eStock</span><span>ePlan</span><span>Preferences</span></nav>
  <div class="abs brandname">BRINDLECOVE</div>

  <nav class="abs subnav"><span class="on">Orders</span><span>Receipes</span><span>Shipments</span><span>Invoices</span><span class="gap"></span><span>Pricing</span><span>Tables</span><span>Reports</span><span>Inquiries</span><span>Periodic Tasks</span><span>Workflows</span></nav>

  <h1 class="abs pagetitle">Purchase Order Lines</h1>
  <div class="abs pagetabs"><span class="on">Header</span><span class="ok">Lines</span><span>Charges</span><span class="ok">Notes</span></div>

  <div class="abs toolbar">
    <svg class="abs" style="left:8px;top:6px" width="18" height="18" viewBox="0 0 18 18"><path d="M12 3 4 11a2.5 2.5 0 0 0 3.5 3.5L15 7" fill="none" stroke="#8fd07a" stroke-width="2"/></svg>
    <svg class="abs" style="left:42px;top:5px" width="20" height="20" viewBox="0 0 20 20"><rect x="2" y="2" width="11" height="14" fill="#fff"/><circle cx="11" cy="12" r="4" fill="none" stroke="#333" stroke-width="2"/><path d="M14 15l4 4" stroke="#fff" stroke-width="2.5"/></svg>
    <svg class="abs" style="left:75px;top:7px" width="22" height="16" viewBox="0 0 22 16"><circle cx="4" cy="11" r="3" fill="#fff"/><circle cx="12" cy="5" r="3" fill="#fff"/><circle cx="19" cy="11" r="3" fill="#fff"/></svg>
    <svg class="abs" style="left:113px;top:6px" width="20" height="18" viewBox="0 0 20 18"><rect x="1" y="5" width="18" height="12" rx="2" fill="#fff"/><rect x="7" y="2" width="6" height="4" fill="none" stroke="#fff" stroke-width="2"/></svg>
    <div class="div" style="left:140px"></div>
    <svg class="abs" style="left:148px;top:7px" width="16" height="16"><circle cx="8" cy="8" r="8" fill="#6c7983"/><text x="8" y="12" font-size="11" text-anchor="middle" fill="#4f5d68" font-family="Arial">?</text></svg>
    <div class="div" style="left:172px"></div>
    <div class="item" style="left:182px"><svg width="20" height="18" viewBox="0 0 20 18"><path d="M2 16 14 4M4 2l12 12" stroke="#fff" stroke-width="2.5"/></svg>View GL Accounts</div>
    <div class="div" style="left:326px"></div>
    <div class="item" style="left:337px"><svg width="20" height="18" viewBox="0 0 20 18"><rect x="1" y="2" width="14" height="12" fill="#fff"/><path d="M3 6h10M3 9h10" stroke="#4f5d68"/><circle cx="15" cy="14" r="4" fill="#5cb85c"/></svg>Post Order</div>
    <div class="div" style="left:688px"></div>
    <div class="item dim" style="left:698px"><svg width="14" height="14"><circle cx="6" cy="6" r="4" fill="none" stroke="#a5adb3" stroke-width="1.6"/><path d="M9 9l4 4" stroke="#a5adb3" stroke-width="1.6"/></svg>search</div>
    <div class="div" style="left:769px"></div>
    <div class="item dim" style="left:778px"><svg width="12" height="12"><circle cx="6" cy="6" r="6" fill="#6a8d6a"/></svg>new</div>
    <div class="div" style="left:832px"></div>
    <div class="item" style="left:842px"><svg width="14" height="12"><path d="M1 6l4 4 8-8" fill="none" stroke="#8fd07a" stroke-width="2.5"/></svg>apply</div>
    <div class="div" style="left:903px"></div>
    <div class="item" style="left:913px"><svg width="12" height="12"><circle cx="6" cy="6" r="6" fill="#e2452b"/><path d="M3.5 3.5l5 5M8.5 3.5l-5 5" stroke="#fff" stroke-width="1.6"/></svg>delete</div>
    <div class="div" style="left:980px"></div>
    <div class="item" style="left:989px"><svg width="14" height="12"><path d="M6 1 1 6l5 5M1 6h8a4 4 0 0 1 4 4" fill="none" stroke="#fff" stroke-width="2"/></svg>back</div>
  </div>

  <section class="abs form">
    <div class="lbl" style="left:70px;top:11px;width:62px">Order #</div>
    <div class="abs" style="left:140px;top:11px;font-family:Arimo,sans-serif;font-size:13px">100159</div>
    <div class="abs green" style="left:263px;top:13px">Regular Purchase Order</div>
    <div class="abs note" style="left:810px;top:12px">Hold For Completion</div>

    <div class="lbl" style="left:40px;top:39px;width:92px">Ship From</div>
    <div class="val" style="left:137px;top:36px;width:102px">1001</div>
    <div class="abs" style="left:244px;top:38px;font-size:13px;font-family:Arimo,sans-serif">/</div>
    <div class="val" style="left:257px;top:36px;width:22px">0</div>

    <div class="val" style="left:137px;top:65px;width:412px">Harborline Medical Co.</div>
    <div class="lbl" style="left:40px;top:90px;width:92px">Address</div>
    <div class="val" style="left:137px;top:88px;width:412px">14 Quarry Lane</div>
    <div class="val" style="left:137px;top:111px;width:412px"></div>
    <svg class="abs" style="left:567px;top:65px" width="24" height="24"><circle cx="12" cy="12" r="11" fill="#e0b574" stroke="#b48440"/><circle cx="12" cy="12" r="5" fill="none" stroke="#a4742e"/></svg>
    <div class="abs" style="left:556px;top:115px;font-family:Arimo,sans-serif;font-size:13px;color:#1a1aff">DPV Unconfirmed</div>

    <div class="lbl" style="left:40px;top:136px;width:92px">City</div>
    <div class="val" style="left:137px;top:134px;width:278px">Eastbrook</div>
    <div class="lbl" style="left:430px;top:136px;width:52px">State</div>
    <div class="val" style="left:486px;top:134px;width:34px">MA</div>
    <svg class="abs" style="left:562px;top:135px" width="14" height="14"><rect x=".5" y=".5" width="13" height="13" fill="#ddd" stroke="#888"/><path d="M3 7l3 3 5-6" fill="none" stroke="#333" stroke-width="1.6"/></svg>
    <div class="abs" style="left:581px;top:134px;font-family:Arimo,sans-serif;font-size:13px">Accept</div>

    <div class="lbl" style="left:40px;top:159px;width:92px">Zip</div>
    <div class="val" style="left:137px;top:157px;width:108px">01872-4410</div>
    <div class="lbl" style="left:270px;top:159px;width:54px">Country</div>
    <div class="val" style="left:330px;top:157px;width:58px">US</div>
    <div class="abs" style="left:459px;top:160px;font-family:Arimo,sans-serif;font-size:13px;text-decoration:underline">Add Contact</div>
  </section>

  <div class="abs inner"></div>
  <div class="abs ftabs"><span>Order Info</span><span class="on">Shipping</span><span>Payment</span><span>Accounts</span><span>Totals / Approval</span></div>

  <div class="lbl" style="left:60px;top:450px;width:104px">Receive At</div>
  <div class="sel" style="left:169px;top:448px;width:115px"><svg width="11" height="7"><path d="M1 1l4.5 4.5L10 1" fill="none" stroke="#222" stroke-width="1.8"/></svg>ALCH</div>
  <span class="req" style="left:286px;top:442px">*</span>
  <div class="lbl" style="left:60px;top:473px;width:104px">Carrier</div>
  <div class="sel" style="left:169px;top:471px;width:115px"><svg width="11" height="7"><path d="M1 1l4.5 4.5L10 1" fill="none" stroke="#222" stroke-width="1.8"/></svg>Swiftline</div>
  <span class="req" style="left:286px;top:465px">*</span>
  <div class="lbl" style="left:40px;top:496px;width:124px">Express Service</div>
  <div class="sel" style="left:169px;top:494px;width:115px"><svg width="11" height="7"><path d="M1 1l4.5 4.5L10 1" fill="none" stroke="#222" stroke-width="1.8"/></svg></div>
  <div class="lbl" style="left:60px;top:519px;width:104px">FOB</div>
  <div class="sel" style="left:169px;top:517px;width:115px"><svg width="11" height="7"><path d="M1 1l4.5 4.5L10 1" fill="none" stroke="#222" stroke-width="1.8"/></svg></div>
  <div class="lbl" style="left:40px;top:542px;width:124px">Order Ship Rule</div>
  <div class="sel" style="left:169px;top:540px;width:144px"><svg width="11" height="7"><path d="M1 1l4.5 4.5L10 1" fill="none" stroke="#222" stroke-width="1.8"/></svg>Partials</div>
  <span class="req" style="left:315px;top:534px">*</span>
  <div class="lbl" style="left:40px;top:565px;width:124px">Line Ship Rule</div>
  <div class="sel" style="left:169px;top:563px;width:144px"><svg width="11" height="7"><path d="M1 1l4.5 4.5L10 1" fill="none" stroke="#222" stroke-width="1.8"/></svg>Partials</div>
  <span class="req" style="left:315px;top:557px">*</span>

  <div class="lbl" style="left:395px;top:450px;width:100px">Request Date</div>
  <div class="abs" style="left:500px;top:448px;width:95px;height:20px;border:1px solid #7a9cd3;font-family:Arimo,sans-serif;font-size:13px;color:var(--field-text);padding:1px 3px">01/07/2018</div>
  <svg class="abs" style="left:597px;top:449px" width="17" height="17"><rect x=".5" y="1.5" width="16" height="15" fill="#e8f1fb" stroke="#5d8fc9"/><rect x="1" y="2" width="15" height="4" fill="#e47a3a"/><path d="M4 9h9M4 12h9" stroke="#7aa4d8"/></svg>
  <div class="lbl" style="left:395px;top:473px;width:100px">Freight Terms</div>
  <div class="sel" style="left:500px;top:471px;width:115px"><svg width="11" height="7"><path d="M1 1l4.5 4.5L10 1" fill="none" stroke="#222" stroke-width="1.8"/></svg>Collect</div>
  <div class="lbl" style="left:395px;top:496px;width:100px">Freight Calc</div>
  <div class="sel" style="left:500px;top:494px;width:158px"><svg width="11" height="7"><path d="M1 1l4.5 4.5L10 1" fill="none" stroke="#222" stroke-width="1.8"/></svg></div>

  <div class="lbl" style="left:690px;top:450px;width:111px">Customer Ship To</div>
  <div class="val" style="left:806px;top:448px;width:88px;background:#f4f4f4"></div>
  <div class="abs" style="left:903px;top:450px;font-family:Arimo,sans-serif;font-size:13px">/</div>
  <div class="val" style="left:902px;top:448px;width:31px;background:#f4f4f4;left:902px;margin-left:0"></div>

  <svg class="abs" style="left:971px;top:645px" width="36" height="44" viewBox="0 0 36 44" role="img" aria-label="Locked record indicator"><path d="M8 20v-7a10 10 0 0 1 20 0v7" fill="none" stroke="var(--lock)" stroke-width="5"/><rect x="2" y="19" width="32" height="24" rx="3" fill="var(--lock)"/><path d="M8 27h20M8 32h20M8 37h20" stroke="#e8d26a" stroke-width="1.5"/></svg>

  <div class="abs status">Click Search, or enter property values and click Apply</div>
</div>
</body>
</html>
```